Manufacturing Company Business card

K & T is a leading supplier of complex machine parts, assemblies and sub assemblies to the aerospace industry.
we would like to create a new feel for our manufacturing company business card design.
We are into lean manufacturing, bold design, metal, use current logo, use "this is your life" logo for entire back of card. updated look for 2015, text, bardcode, etc

our primary end use is flight control components used on about all commercial and business jets in use as well as military aircraft and civil aviation.

Reason: Need more time to review with internal team at KTmfg:)

Target Market(s)

aerospace, manufacturing

Industry/Entity Type

Aero

Contact Information for Business Card

New, industrial, trendy, use current logo, we like text, vmail is lame :( cell ph is ok - what is a fax???

Font styles to use
Serif
Sans Serif

Requirements
Must have
• incorporate our current logo, one option is an Industrial look, metal etc. we can also try to incorporate the feel of the back of the card onto the front but not so busy.
• Back of card full size "this is your life"
• front side, barcode, cell, - our motto "solutions in manufacturing" tm
Nice to have
• Professional look
• up to date
• appeals to broad audience
Should not have
• too much content - pictures of planes

```html
<!DOCTYPE html>
<html lang="en">
<head>
<meta charset="utf-8">
<title>K &amp; T Manufacturing – Business Card</title>
<link href="https://fonts.googleapis.com/css2?family=Raleway:wght@400;600&display=swap" rel="stylesheet">
<style>
  :root {
    --stage: #1b1b1c;
    --card: #2e2f33;
    --ghost: #393a3e;
    --brand-text: #ececec;
    --ring: #d8d8d8;
    --name: #55b05a;
    --role: #b4b4b4;
    --contact: #cfcfcf;
  }
  * { box-sizing: border-box; margin: 0; padding: 0; }
  html, body {
    width: 1200px;
    height: 900px;
    overflow: hidden;
    background: var(--stage);
    font-family: "Raleway", sans-serif;
  }
  .card {
    position: absolute;
    left: 331px;
    width: 542px;
    height: 315px;
    background: var(--card);
    border-radius: 14px;
    overflow: hidden;
  }
  .card--front { top: 121px; }
  .card--back  { top: 489px; }

  .brand {
    position: absolute;
    display: flex;
    align-items: center;
    gap: 14px;
    color: var(--brand-text);
    font-weight: 600;
    letter-spacing: 0.5px;
    white-space: nowrap;
  }
  .brand__ring {
    flex: none;
    border: 2px solid var(--ring);
    border-radius: 50%;
  }
  .card--front .brand { left: 40px; top: 72px; font-size: 26px; }
  .card--front .brand__ring { width: 42px; height: 42px; }
  .card--back .brand { left: 82px; top: 136px; font-size: 28px; }
  .card--back .brand__ring { width: 46px; height: 46px; }

  .ghost-mark {
    position: absolute;
    left: 10px;
    top: 196px;
    font-size: 66px;
    font-weight: 600;
    line-height: 1;
    color: var(--ghost);
    white-space: nowrap;
  }

  .contact {
    position: absolute;
    left: 213px;
    top: 174px;
  }
  .contact__name {
    font-size: 25px;
    font-weight: 400;
    color: var(--name);
    line-height: 1.1;
  }
  .contact__role {
    font-size: 16px;
    color: var(--role);
    margin-top: 2px;
  }
  .contact__lines {
    list-style: none;
    margin-top: 18px;
    font-size: 14px;
    line-height: 19px;
    color: var(--contact);
  }
</style>
</head>
<body>
  <section class="card card--front" aria-label="Card front">
    <div class="ghost-mark" aria-hidden="true">K &amp; T</div>
    <div class="brand">
      <span class="brand__ring" aria-hidden="true"></span>
      <span class="brand__name">K &amp; T MANUFACTURING</span>
    </div>
    <div class="contact">
      <p class="contact__name">Daniel Moore</p>
      <p class="contact__role">Managing Director</p>
      <ul class="contact__lines">
        <li>hello@ktmfg.example</li>
        <li>044-987 650 321</li>
      </ul>
    </div>
  </section>

  <section class="card card--back" aria-label="Card back">
    <div class="brand">
      <span class="brand__ring" aria-hidden="true"></span>
      <span class="brand__name">K &amp; T MANUFACTURING</span>
    </div>
  </section>
</body>
</html>
```